Business Card Design Project

HI! Can you design a business card with the logo you designed for me? I don't know what the typical order is so can you place it in the order most people do? White background and also play with a couple of colored backgrounds. Thank you!

Darnel Quesvo-Tranetti
darnel@tovenashcoaching.example
tovenashcoaching.example
555-317-4809

Target Market(s)

Women

Industry/Entity Type

Business

```html
<!DOCTYPE html>
<html lang="en">
<head>
<meta charset="UTF-8">
<title>Tovenash Coaching Services – Business Card</title>
<link rel="stylesheet" href="https://fonts.googleapis.com/css2?family=Roboto+Condensed:wght@300;400;700&display=swap">
<style>
  :root {
    --stage: #4a4a4a;
    --card-red: #be1e2d;
    --card-white: #ffffff;
    --ink-light: #ffffff;
    --brand-red: #be1e2d;
    --brand-orange: #f6921e;
  }
  * { margin: 0; padding: 0; box-sizing: border-box; }
  html, body {
    width: 900px;
    height: 1200px;
    overflow: hidden;
    background: var(--stage);
    font-family: "Roboto Condensed", Arial, sans-serif;
  }
  .business-card {
    position: absolute;
    left: 228px;
    top: 236px;
    width: 433px;
    height: 736px;
    border-radius: 12px;
    overflow: hidden;
    background: var(--card-white);
  }
  .contact-panel {
    position: absolute;
    left: 0;
    top: 0;
    width: 100%;
    height: 411px;
    background: var(--card-red);
    color: var(--ink-light);
  }
  .holder-name {
    position: absolute;
    left: 91px;
    top: 196px;
    font-size: 35px;
    font-weight: 300;
    line-height: 1;
    white-space: nowrap;
  }
  .name-rule {
    position: absolute;
    left: 91px;
    top: 243px;
    width: 255px;
    height: 2px;
    background: var(--ink-light);
  }
  .contact-line {
    position: absolute;
    left: 91px;
    font-size: 18px;
    font-weight: 300;
    line-height: 1;
    white-space: nowrap;
  }
  .contact-email { top: 252px; }
  .contact-web { top: 276px; }
  .contact-phone {
    top: 305px;
    font-size: 19px;
    font-weight: 700;
  }
  .brand-block {
    position: absolute;
    left: 0;
    top: 411px;
    width: 100%;
    height: 325px;
    text-align: center;
  }
  .brand-dot {
    position: absolute;
    left: 166px;
    top: 51px;
  }
  .brand-name {
    position: absolute;
    left: 0;
    width: 100%;
    color: var(--brand-red);
    font-weight: 400;
    line-height: 1;
  }
  .brand-name-main {
    top: 182px;
    font-size: 54px;
  }
  .brand-name-sub {
    top: 244px;
    font-size: 20px;
    letter-spacing: 4px;
    text-transform: uppercase;
  }
</style>
</head>
<body>
  <main class="business-card">
    <section class="contact-panel">
      <h1 class="holder-name" style="font-weight:300">Darnel Quesvo-Tranetti</h1>
      <div class="name-rule"></div>
      <p class="contact-line contact-email">darnel@tovenashcoaching.example</p>
      <p class="contact-line contact-web">tovenashcoaching.example</p>
      <p class="contact-line contact-phone">Touch With Us: 555-317-4809</p>
    </section>
    <section class="brand-block">
      <svg class="brand-dot" width="102" height="102" viewBox="0 0 102 102" aria-hidden="true">
        <circle cx="51" cy="51" r="46" fill="var(--brand-orange)" stroke="var(--brand-red)" stroke-width="1.5"/>
      </svg>
      <p class="brand-name brand-name-main">Tovenash</p>
      <p class="brand-name brand-name-sub">Coaching Services</p>
    </section>
  </main>
</body>
</html>
```